KREPvalMusic & KREPvalGuitarLessons Website
Music teaching.
KREPvalMusic & KREPvalGuitarLessons Website - Music
Creative Brief
Music
www.krepvalmusic.example
KREP Val Music is a company that will house 5 different businesses
1) KREP Val Online Music Lessons
2) KREP Val Publishing (for my 2 books)
3) KREP Val Recording
4) KREP Val Production
5) KREP Val Guitar Lessons.
Each of these will have a separate website, I have all the domain names already registered. Each website will look and feel the same, only the website name will differ for each individual business.
Here's some trivia that might be inspiring:
KREP (has many different meaning in Flemish and Dutch): it means anywhere from "Being in Love", to also meaning "unconventional", "crazy" (in any possible form and meaning of that word), but also "mentally unstable", "impressive", etc...
Val: different meanings as well... "Meaning" (as in for example "meaning of life", it also means "sentence" (as in sentences in a language), it also means "lust" (ohh yeahhh haha), "liking", "setting your mind to something", etc...
In combination, the word "Val" in Flemish means "to be"... so literally translated as whole, from Flemish... this would mean" "To Be Crazy".
My main reason for this business name, when I brainstormed this because I needed one, was that it stands out and is memorable with the 2 Z's
AND
It was important to me that the words would be short enough so English speaking people would pronounce the words EXACTLY as they are pronounced in Flemish and Dutch... which is the case. Yaaaay.
Message my company and my website wants to convey:
1) "Fun" is serious business fpr KREP Val Music.
2) KREP Val Music rocks your world.
3) We are creative and inventive
4) YOU are important to us (the bigger head/globe creates that impression strongly)
5) You can "belt" out with us without and be yourself and we help you find your voice.
6) We work focused and structured, but are not rigid. (the falling letters at the end of the logo, being support by the word "music")... we have a plan and direction, and vision, but easily adapt our approach to your needs. I think the design manages to evoke that pretty well... it looks playful but has some sense of balance and structure in it as well.
7) We are fun to work with, flexible and we get things done
This post is for the creation of the guitar lessons website www.KREPvalGuitarLessons.example
"KREP Val Guitar Lessons" offers personalized private guitar instruction incorporating principles of super-study, psychology, music pedagogy, time management & neuroscience
I like the idea of having the tagline/sales line...
"From Fretfumble to Fretfame"
underneath the logo.
I LOVE everything about Quince and I also love their website. It has a cool feeling of space, design, and nice graphics. I want my site to have the same sophisticated, clean, fresh, clear, open feel like the Quince website. I want black text on white background. I want the whole website to be entirely visible without needing to scroll. I would dislike my website looking too much like a template or Pagesmith template. I want it to look like it's custom designed. I want following links/navigation: 1) home I probably would provide the same info like this guy http://www.strumschoolbay.example/faq.htm 2) About Lorsa 3) The Lessons 4) Tuition 5) Testimonials 6) Support 7) FAQ 8) Gallery. Then there is info I want on every page. 1) Contact info. (as on http://www.strumschoolbay.example/faq.htm) Following 7 things that I want on every page, I would like this info like on the Quince website, in cool little link boxes at the bottom of each page, that you click on and a new page then opens up from there. ( I have attached/uploaded a picture called "link boxes), which I took from the quince website to showcase what I mean. I want to have a cool, glossy, sophisticated graphic in every link box/button, just like on the quince website) 2) A box for a student testimonial on top of every page: 3) a Free Resources box: This would be a newsletter, in the form of a little content box showing up on every page with a link. (Which will lead to an info page) (as in http://doratelvik.example/resources/) 4) a box/button that says: "What’s Your Sticking Point?" 5) A 30 second Video Tips. box 6) a Social Networking box. This would be a box that holds links (as icons) where students can further connect to me on my Chatterly, Peepline, Vidcove etc page. 7) A “Buy Now” link/button or box with a link to CoinPost on EVERY page (besides obviously the tuition page) so visitors can buy their lessons from any page). 8) Subscribe boxes: (which would be linked to different email campaigns ). 9) a box labeled "The Challenge" I like having all my contact info in the header, like here http://www.strumschoolbay.example/index.html But I dislike headers that big... I want my header to take up little space on the page, like here http://www.quince.example/ (but maybe a tad bigger than this, as my logo will have to fit in the header)
White
Blue Greenish color as in my logo
Silverish
below header
http://www.quince.example/
http://www.strumschoolbay.example/index.html
http://doratelvik.example/
I want the site to have a glossy, sophisticated look, but every organized, structured and easy to navigate.

```html
<!DOCTYPE html>
<html lang="en">
<head>
<meta charset="utf-8">
<title>KREPval Guitar Lessons</title>
<link rel="stylesheet" href="https://fonts.googleapis.com/css2?family=Arimo:ital,wght@0,400;0,700;1,400&family=Oswald:wght@300;400;500&display=swap">
<style>
:root{
  --teal:#1a9bb8;
  --teal-dark:#0f7f99;
  --ink:#2b2b2b;
  --grey:#5a5a5a;
  --silver:#d9dcde;
  --silver-light:#eef0f1;
  --bar:#2a2d30;
  --bar-hi:#4a4e52;
  --orange:#c98a2c;
  --blue-word:#2e74b5;
  --paper:#ffffff;
}
*{box-sizing:border-box;margin:0;padding:0}
html,body{width:1200px;height:857px;overflow:hidden}
body{font-family:"Arimo",Arial,sans-serif;color:var(--ink);
  background:linear-gradient(180deg,#f7f8f8 0%,#e9ebec 60%,#dfe2e4 100%)}
.stage{position:relative;width:1200px;height:857px}

/* header */
.brand{position:absolute;left:160px;top:40px;display:flex;align-items:center;gap:12px}
.brand-dot{width:34px;height:34px;border-radius:50%;background:var(--teal)}
.brand-name{font-family:"Arimo",Arial,sans-serif;font-weight:700;font-size:22px;line-height:26px;color:var(--ink);text-transform:uppercase;letter-spacing:1px;width:210px}
.tagline{position:absolute;left:430px;top:30px;font-family:"Oswald",sans-serif;font-weight:400;font-size:31px;line-height:34px;color:#3a3a3a;letter-spacing:1px;text-align:center;width:310px}
.tagline span{display:block}
.contact{position:absolute;left:780px;top:26px;width:280px;height:80px}
.contact svg{position:absolute;left:0;top:4px}
.contact-text{position:absolute;left:62px;top:0;text-align:left}
.contact-cta{font-size:15px;color:var(--teal)}
.contact-phone{font-family:"Oswald",sans-serif;font-size:31px;line-height:36px;color:#222}
.contact-mail{font-size:14px;color:#555}

/* nav */
.nav{position:absolute;left:149px;top:108px;width:902px;height:36px;display:flex;border-radius:4px;overflow:hidden;
  background:linear-gradient(180deg,var(--bar-hi) 0%,var(--bar) 55%,#1c1e20 100%)}
.nav a{flex:1;display:flex;align-items:center;justify-content:center;color:#fff;text-decoration:none;font-size:15px;font-weight:700;border-right:1px solid #444}
.nav a:last-child{border-right:none}
.nav a.active{background:linear-gradient(180deg,#4cc0dc 0%,var(--teal) 55%,var(--teal-dark) 100%)}

/* hero */
.hero{position:absolute;left:149px;top:156px;width:902px;height:384px;border-radius:6px;overflow:hidden;
  background:linear-gradient(90deg,#f2f3f4 0%,#ffffff 55%,#f4f5f6 100%);box-shadow:0 1px 4px rgba(0,0,0,.25)}
.hero-photo{position:absolute;left:0;top:0;width:470px;height:384px;
  background:radial-gradient(ellipse at 45% 40%,#ffffff 0%,#e4e6e8 45%,#b8bcc0 80%,#8f9397 100%)}
.hero-copy{position:absolute;left:480px;top:24px;width:392px;height:336px;background:rgba(255,255,255,.92);
  border:1px dashed #b7b7b7;padding:14px 20px}
.hero-head{font-family:"Oswald",sans-serif;font-weight:300;font-size:26px;line-height:30px;color:#444;text-transform:uppercase}
.hero-head .w1{color:var(--teal);font-weight:400}
.hero-head .w2{color:var(--blue-word);font-weight:400}
.hero-copy p{font-size:12.5px;line-height:16px;color:var(--orange);margin-top:10px}
.hero-sign{position:absolute;right:20px;bottom:10px;font-family:"Oswald",sans-serif;font-size:17px;color:var(--orange);letter-spacing:1px}
.arrow{position:absolute;top:322px;width:28px;height:28px;background:#2a2d30;border-radius:3px;display:flex;align-items:center;justify-content:center}
.arrow.prev{left:138px}.arrow.next{left:1034px}

/* link boxes */
.boxes{position:absolute;left:149px;top:548px;width:902px;height:172px;display:flex;gap:6px}
.box{position:relative;flex:1;background:linear-gradient(180deg,#ffffff 0%,var(--silver-light) 100%);border:1px solid #c8cbce;border-radius:4px;padding:10px 12px}
.box-title{font-size:14px;font-weight:700;color:#222;text-transform:uppercase;white-space:nowrap}
.box-sub{font-size:13px;color:var(--teal)}
.box-text{font-size:12px;line-height:16px;color:#444;margin-top:6px;width:108px}
.box-text em{display:block;color:var(--teal);font-style:normal;margin-top:6px}
.box-art{position:absolute;right:12px;top:36px;width:78px;height:78px;border-radius:8px}
.art-chat{background:radial-gradient(circle at 40% 40%,#8fd3e6 0%,var(--teal) 70%)}
.art-phones{background:radial-gradient(circle at 45% 40%,#f2a49b 0%,#c8352a 55%,#3a3a3a 100%)}
.video{position:absolute;left:10px;top:34px;width:200px;height:104px;border-radius:3px;background:linear-gradient(135deg,#7b5a3c 0%,#3b2c22 60%,#1e1814 100%)}
.btn{position:absolute;left:50%;transform:translateX(-50%);bottom:10px;width:112px;height:22px;border-radius:11px;
  background:linear-gradient(180deg,#4a4e52 0%,#1f2123 100%);color:#fff;font-size:11px;font-weight:700;display:flex;align-items:center;justify-content:center;gap:6px}
.btn i{width:12px;height:12px;border-radius:50%;background:var(--teal);display:inline-block}
.email{position:absolute;left:12px;top:96px;width:198px;height:24px;border:1px solid #bbb;background:#fff;font-size:11px;color:#999;padding:5px 6px}

/* strip */
.strip{position:absolute;left:149px;top:732px;width:902px;height:60px;display:flex;gap:6px}
.cell{position:relative;flex:1;background:linear-gradient(180deg,#ffffff 0%,var(--silver-light) 100%);border:1px solid #c8cbce;border-radius:4px;padding:10px 12px}
.cell-title{font-size:13px;font-weight:700;color:#333;text-transform:uppercase}
.cell-sub{font-size:13px;color:var(--teal)}
.cell-art{position:absolute;right:18px;top:10px;width:40px;height:40px;border-radius:50%}
.art-star{background:radial-gradient(circle at 40% 35%,#bfe7f2 0%,var(--teal) 75%)}
.art-cup{background:radial-gradient(circle at 40% 35%,#cfe4f2 0%,#4b8fc4 75%)}
.buy{display:flex;align-items:center;gap:26px}
.buy .cell-title{font-size:16px;color:#555}
.coin{font-size:22px;font-weight:700;color:#1e4f8c}
.social{display:flex;align-items:center;justify-content:space-around;padding:8px 6px}
.soc{display:flex;flex-direction:column;align-items:center;gap:3px;font-size:9px;color:#444}
.soc b{width:28px;height:28px;border-radius:4px;background:var(--sq)}

/* footer */
.footer{position:absolute;left:158px;top:815px;width:884px;display:flex;justify-content:space-between;font-size:11.5px;color:#555}
.footer nav a{color:var(--teal-dark);text-decoration:none}
.footer nav span{margin:0 4px;color:#888}
.baseline{position:absolute;left:0;top:842px;width:1200px;height:15px;background:linear-gradient(180deg,#cfd3d6,#b4b9bd)}
</style>
</head>
<body>
<div class="stage">

  <header>
    <div class="brand">
      <div class="brand-dot"></div>
      <div class="brand-name">KREPval Guitar Lessons</div>
    </div>
    <div class="tagline"><span>FROM FRETFUMBLE</span><span>TO FRETFAME</span></div>
    <div class="contact">
      <svg width="50" height="56" viewBox="0 0 50 56" aria-hidden="true">
        <rect x="2" y="14" width="46" height="38" rx="5" fill="#2a2d30"/>
        <path d="M8 16 Q25 -2 42 16" fill="none" stroke="#2a2d30" stroke-width="7"/>
        <rect x="13" y="22" width="24" height="24" rx="3" fill="#555"/>
        <circle cx="19" cy="28" r="2" fill="#ddd"/><circle cx="25" cy="28" r="2" fill="#ddd"/><circle cx="31" cy="28" r="2" fill="#ddd"/>
        <circle cx="19" cy="34" r="2" fill="#ddd"/><circle cx="25" cy="34" r="2" fill="#ddd"/><circle cx="31" cy="34" r="2" fill="#ddd"/>
        <circle cx="19" cy="40" r="2" fill="#ddd"/><circle cx="25" cy="40" r="2" fill="#ddd"/><circle cx="31" cy="40" r="2" fill="#ddd"/>
      </svg>
      <div class="contact-text">
        <div class="contact-cta">Get Started! Contact Us Today</div>
        <div class="contact-phone">1.(555).204.7731</div>
        <div class="contact-mail">info@krepvalmusic.example</div>
      </div>
    </div>
  </header>

  <nav class="nav">
    <a class="active" href="#">About Lorsa</a>
    <a href="#">The Lessons</a>
    <a href="#">Tuition</a>
    <a href="#">Testimonials</a>
    <a href="#">Support</a>
    <a href="#">FAQ</a>
    <a href="#">Gallery</a>
  </nav>

  <section class="hero">
    <div class="hero-photo" role="img" aria-label="Close-up photograph of an acoustic guitar neck and strings"></div>
    <div class="hero-copy">
      <h1 class="hero-head">We are fun to <span class="w1">work</span> with,<br><span class="w2">flexible</span> and we get things done</h1>
      <p>KREP means anywhere from "Being in Love", to "unconventional", "crazy" (in any possible meaning of that word), but also "impressive" or out there.</p>
      <p>Val. In Dutch means "Meaning" (as in for example: "the meaning of life"). It also means "sentence" (as in: a series of words), but also "lust" or "liking".</p>
      <p>In combination with KREP, the word "Val" in Flemish, means "to be".</p>
      <p>This site is for those who tend "To Be Crazy"</p>
      <div class="hero-sign">ABOUT MUSIC.</div>
    </div>
  </section>
  <div class="arrow prev"><svg width="12" height="14" viewBox="0 0 12 14"><path d="M10 1 L2 7 L10 13 Z" fill="#fff"/></svg></div>
  <div class="arrow next"><svg width="12" height="14" viewBox="0 0 12 14"><path d="M2 1 L10 7 L2 13 Z" fill="#fff"/></svg></div>

  <section class="boxes">
    <article class="box">
      <h2 class="box-title">Testimonials</h2>
      <p class="box-text">Lorem Ipsum is simply dummy text of the printing.<em>Writer's Name</em></p>
      <div class="box-art art-chat" role="img" aria-label="Glossy speech bubbles graphic"></div>
      <div class="btn"><i></i>READ MORE</div>
    </article>
    <article class="box">
      <h2 class="box-title">Free Resources</h2>
      <p class="box-text">Lorem ipsum dolor sit amet, consect&shy;etur adipiscing elit, sed do eiusmod.</p>
      <div class="box-art art-phones" role="img" aria-label="Glossy headphones and book graphic"></div>
      <div class="btn"><i></i>READ MORE</div>
    </article>
    <article class="box">
      <h2 class="box-title">Video Tips</h2>
      <div class="video" role="img" aria-label="Video thumbnail of a guitar lesson"></div>
    </article>
    <article class="box">
      <h2 class="box-title">Subscribe Newsletter</h2>
      <div class="box-sub">to the KREPval.example</div>
      <div class="email">Enter Email Address...</div>
      <div class="btn"><i></i>SUBSCRIBE</div>
    </article>
  </section>

  <section class="strip">
    <div class="cell">
      <div class="cell-title">What's your</div>
      <div class="cell-sub">STICKING POINT?</div>
      <div class="cell-art art-star" role="img" aria-label="Glossy star graphic"></div>
    </div>
    <div class="cell">
      <div class="cell-title">The Challenge</div>
      <div class="cell-sub">Are you up for it?</div>
      <div class="cell-art art-cup" role="img" aria-label="Glossy trophy graphic"></div>
    </div>
    <div class="cell buy">
      <div class="cell-title">Buy Now</div>
      <div class="coin">CoinPost</div>
    </div>
    <div class="cell social">
      <div class="soc"><b style="--sq:#3b5a98"></b>Chatterly</div>
      <div class="soc"><b style="--sq:#3fa9d8"></b>Peepline</div>
      <div class="soc"><b style="--sq:#c4302b"></b>Vidcove</div>
      <div class="soc"><b style="--sq:#f08a24"></b>Feed</div>
    </div>
  </section>

  <footer class="footer">
    <nav><a href="#">About Lorsa</a><span>|</span><a href="#">Sitemap</a><span>|</span><a href="#">FAQ</a><span>|</span><a href="#">Support</a><span>|</span><a href="#">Contacts</a></nav>
    <div>© 2011. KREPval.example. All rights reserved</div>
  </footer>
  <div class="baseline"></div>
</div>
</body>
</html>
```